Home Improvement Company in need of a "Banner & Billboard Design"

I'm Looking for a Banner design 4X6 With Company Logo, Phone Number, website, Credentials and services.. I picture a charcoal/matte background i also want to look like a house shape design i will upload the sample...

I'm looking for a Billboard design to target homeowners who need Roofing Services. I need logo, number, website, KTL, Credentials and a catchy title. i will like to use the same colors for branding

Target Market(s)

Homeowners, Investors,

Industry/Entity Type

Home Improvement

Font styles to use
Decorative

Colors
00a990
5c5c5c
333333

Requirements
Must have
• All Credentials, Phone number, website, logo, logo colors, services, Eye Catchy, Direct Message, Friendly feeling,
• (614) 372 - 9058
• Roofing Gutters Painting Pressure Washing Exterior Design
Nice to have
• A catchy title, A direct message to a homeowner looking for home improvement services. noticeable
Should not have
• not Busy, no

```html
<!DOCTYPE html>
<html lang="en">
<head>
<meta charset="utf-8">
<title>Harbor Home Exteriors — Billboard</title>
<link href="https://fonts.googleapis.com/css2?family=Cinzel:wght@600;700&family=Open+Sans:wght@700;800&display=swap" rel="stylesheet">
<style>
  :root{
    --teal:#1d9485;
    --teal-bright:#00a990;
    --charcoal:#333333;
    --slate:#5c5c5c;
    --roof:#1c1c1c;
    --wall:#ffffff;
    --backdrop:#e4e4e4;
    --badge-red:#d8262c;
    --badge-blue:#1c5ea8;
  }
  *{margin:0;padding:0;box-sizing:border-box}
  html,body{width:1200px;height:1200px;overflow:hidden;background:var(--backdrop)}
  .billboard{position:relative;width:1200px;height:1200px}
  .house{position:absolute;inset:0}
  .brand{position:absolute;left:340px;top:300px;width:440px;text-align:center;font-family:"Cinzel",serif}
  .brand-mark{display:inline-block;width:34px;height:34px;background:var(--teal);margin-bottom:10px}
  .brand-name{font-weight:700;font-size:40px;line-height:1.05;color:var(--teal);letter-spacing:1px}
  .brand-tagline{font-weight:600;font-size:17px;letter-spacing:3px;color:var(--slate);margin-top:8px}
  .services{position:absolute;left:190px;top:500px;width:790px;font-family:"Open Sans",sans-serif;font-weight:800;color:#fff;font-size:31px;letter-spacing:1px;text-transform:uppercase}
  .services-row{display:flex;gap:34px;margin-bottom:10px}
  .services-row.second{padding-left:0}
  .service::before{content:"›";color:var(--teal-bright);margin-right:10px;font-size:38px;line-height:0}
  .contact{position:absolute;left:140px;top:625px;font-family:"Open Sans",sans-serif;font-weight:800;color:#fff}
  .contact-phone{font-size:94px;line-height:1.05;letter-spacing:1px}
  .contact-web{font-size:60px;line-height:1.1}
  .credentials{position:absolute;left:320px;top:890px;display:flex;align-items:center;gap:40px}
  .badge-cert{width:190px;height:62px;background:var(--badge-red);border-top:14px solid #8a8a8a}
  .badge-maker{width:72px;height:68px;background:var(--badge-red)}
  .badge-listing{width:46px;height:70px;background:#fff;border:3px solid var(--badge-blue)}
</style>
</head>
<body>
<div class="billboard">
  <svg class="house" width="1200" height="1200" viewBox="0 0 1200 1200" aria-hidden="true">
    <rect x="770" y="170" width="80" height="120" fill="var(--roof)"/>
    <polygon points="100,470 560,150 1100,430 1100,480 560,205 100,520" fill="var(--roof)"/>
    <polygon points="100,520 560,205 1100,480 1100,1010 100,1010" fill="var(--wall)"/>
    <rect x="160" y="470" width="840" height="400" fill="var(--charcoal)"/>
    <rect x="100" y="612" width="1000" height="210" fill="var(--teal)"/>
  </svg>

  <div class="brand">
    <span class="brand-mark"></span>
    <div class="brand-name">Harbor Home Exteriors</div>
    <div class="brand-tagline">WHEN QUALITY MATTERS.</div>
  </div>

  <div class="services">
    <div class="services-row"><span class="service">Roofing</span><span class="service">Gutters</span><span class="service">Painting</span></div>
    <div class="services-row second"><span class="service">Pressure Washing</span><span class="service">Exterior Design</span></div>
  </div>

  <div class="contact">
    <div class="contact-phone">(614) 372 - 9058</div>
    <div class="contact-web">HarborHomeExteriors.com</div>
  </div>

  <div class="credentials">
    <div class="badge-cert" role="img" aria-label="Certified roofing contractor badge"></div>
    <div class="badge-maker" role="img" aria-label="Roofing manufacturer partner badge"></div>
    <div class="badge-listing" role="img" aria-label="KTL accredited business badge"></div>
  </div>
</div>
</body>
</html>
```